Corporate speaking flyer for email

Redesign existing and very lame flyer. This is for my speaking business to be used as an introduction of content and style and my presentations. More photos can be provided. As you will see I'm an adventurer who makes part of my living from speaking about my adventures. The bio describes the general gist of that. There is more I could say but wanting to keep it pretty brief so as not to bore potential clients. Having said that I'd like to try and capture them in the first instance.

Target Market(s)

Corporate, clubs, events

Industry/Entity Type

Business

Requirements
Must have
• bio and references. Content provided. Feel free to edit.
Nice to have
• Surprise me!
Should not have
• Rude words.

```html
<!DOCTYPE html>
<html lang="en">
<head>
<meta charset="utf-8">
<title>Sam Dalton – Speaker Flyer</title>
<link href="https://fonts.googleapis.com/css2?family=Oswald:wght@600&family=Noto+Serif:ital@1&family=Jost:wght@400;600&display=swap" rel="stylesheet">
<style>
  :root {
    --page-bg: #7f9796;
    --panel: #141212;
    --panel-edge: #3a3838;
    --ribbon: #1d2a6e;
    --ribbon-dark: #121b4d;
    --band: #2a3470;
    --band-light: #47508a;
    --text: #ffffff;
    --text-soft: #e6e6e6;
    --photo-light: #c9c9c9;
    --photo-dark: #2b2b2b;
  }
  * { box-sizing: border-box; margin: 0; padding: 0; }
  html, body { width: 1200px; height: 960px; overflow: hidden; }
  body { background: var(--page-bg); font-family: "Jost", sans-serif; position: relative; }

  .flyer {
    position: absolute; left: 283px; top: 30px;
    width: 634px; height: 900px;
    background: #f2f2f2;
    overflow: hidden;
  }
  .flyer__photo {
    position: absolute; left: 0; top: 0; width: 269px; height: 847px;
    background: linear-gradient(180deg, #9a9a9a 0%, var(--photo-light) 35%, #8a8a8a 60%, var(--photo-dark) 78%, #d8d8d8 100%);
  }
  .flyer__panel {
    position: absolute; left: 269px; top: 0; width: 348px; height: 847px;
    background: var(--panel);
  }
  .flyer__edge {
    position: absolute; left: 617px; top: 0; width: 17px; height: 847px;
    background: linear-gradient(90deg, var(--panel-edge), #bdbdbd);
  }
  .speaker-name {
    position: absolute; left: 269px; width: 348px; top: 28px;
    text-align: center; color: var(--text);
    font-family: "Oswald", sans-serif; font-weight: 600; font-size: 32px; letter-spacing: 0.5px;
  }
  .tagline {
    position: absolute; left: 262px; top: 86px; width: 362px; height: 40px;
    background: linear-gradient(180deg, var(--ribbon) 0%, var(--ribbon-dark) 100%);
    color: var(--text); text-align: center;
    font-family: "Noto Serif", serif; font-style: italic; font-size: 24px; line-height: 40px;
  }
  .bio {
    position: absolute; left: 287px; top: 146px; width: 314px;
    color: var(--text-soft); font-size: 10.2px; line-height: 12.8px; letter-spacing: 0.15px; text-align: justify;
  }
  .bio p { margin-bottom: 11px; }
  .bio strong { color: var(--text); font-weight: 600; }
  .contact-phone {
    position: absolute; left: 269px; width: 348px; top: 740px;
    text-align: center; color: var(--text);
  }
  .contact-phone svg { display: block; margin: 0 auto 6px; }
  .contact-phone p { font-size: 24px; line-height: 33px; letter-spacing: 0.5px; }
  .contact-band {
    position: absolute; left: 0; top: 847px; width: 634px; height: 44px;
    background: linear-gradient(180deg, var(--band-light) 0%, var(--band) 100%);
    color: var(--text); font-size: 15px;
    display: flex; align-items: center; justify-content: space-between; padding: 0 24px 0 26px;
  }
  .contact-band__item { display: flex; align-items: center; gap: 12px; }
</style>
</head>
<body>
  <main class="flyer">
    <div class="flyer__photo" role="img" aria-label="Black and white photo of the speaker presenting on stage to a seated audience"></div>
    <div class="flyer__panel"></div>
    <div class="flyer__edge"></div>

    <h1 class="speaker-name">SAM DALTON</h1>
    <h2 class="tagline">Anything is Possible</h2>

    <section class="bio">
      <p>Whether it's laugh out loud humour, inspiration or thought provoking anecdotes and perspective, Sam Dalton's deeply moving presentations has it all.</p>
      <p>"An extraordinary mental and physical effort – something very, very special" is how Sir Ian Marsh described Sam Dalton and the late Ned Corliss' incredible achievement in winning the inaugural Meridian Ocean Row.</p>
      <p>Marathon rowing champion Sam Dalton has been an international rowing representative for many years. Sam's numerous rowing achievements include world championship medals, a major games title and a record on the indoor rowing machine.</p>
      <p>Sam raced at international regattas and published 'Oars and Open Water' on how he and Ned Corliss captured headlines winning the grueling and inaugural Meridian Ocean Row in a record crossing. He then led crews to successful defenses in the next two editions, making it a hat-trick of victories.</p>
      <p>He is co-organiser of the 'River 100' (www.river100.example) and 'The River Crew Race' (<strong>www.rivercrewrace.example</strong>), an annual rowing eights clash between local and visiting university crews on his home river. He also recently conceived and managed a long-distance rowing expedition along the coast.</p>
      <p>Ambitious goal-setting, teamwork and overcoming adversity in multiple ocean rowing campaigns is the spine of Sam's presentations, sandwiching the challenge of retracing his father's lost trek across a remote northern range <strong>www.thelongsearch.example</strong> (optional topic). Powerful inspiring messages on tenacity, hope, love and the last human freedom: the power to choose your attitude and how you respond in a given situation. The humour, the insights and the emotional turning points have audiences spellbound.</p>
      <p>Sam will inspire you to pursue your dreams whatever they may be, to take on new challenges, overcoming hardship against the odds and know that with passion anything is possible!</p>
      <p><strong>It doesn't hurt to be just a little bit crazy too!</strong></p>
      <p>Sam's life is about following the dream, decision making, commitment, team building, goal setting, planning, focus, determination, positive thinking and, of course, winning!</p>
    </section>

    <div class="contact-phone">
      <svg width="24" height="24" viewBox="0 0 24 24" aria-hidden="true">
        <circle cx="12" cy="12" r="10.5" fill="none" stroke="#fff" stroke-width="1.5"/>
        <path d="M8.6 6.8l1.6-.4 1.1 2.6-1.2 1c.6 1.4 1.6 2.5 3 3.1l1-1.2 2.6 1.1-.4 1.6c-.2.7-.9 1.1-1.6 1-3.6-.6-6.4-3.4-7-7-.1-.7.3-1.4.9-1.8z" fill="#fff"/>
      </svg>
      <p>+64 (0)21 555 01234</p>
      <p>+64 (0)7 555 0187</p>
    </div>

    <footer class="contact-band">
      <div class="contact-band__item">
        <svg width="20" height="20" viewBox="0 0 20 20" aria-hidden="true">
          <circle cx="10" cy="10" r="9" fill="none" stroke="#fff" stroke-width="1.2"/>
          <rect x="5" y="6.5" width="10" height="7" fill="none" stroke="#fff" stroke-width="1.2"/>
          <path d="M5 6.5l5 4 5-4" fill="none" stroke="#fff" stroke-width="1.2"/>
        </svg>
        <span>sam@tidemail.example</span>
      </div>
      <div class="contact-band__item">
        <svg width="20" height="20" viewBox="0 0 20 20" aria-hidden="true">
          <circle cx="10" cy="10" r="9" fill="none" stroke="#fff" stroke-width="1.2"/>
          <circle cx="10" cy="10" r="5.5" fill="none" stroke="#fff" stroke-width="1"/>
          <ellipse cx="10" cy="10" rx="2.3" ry="5.5" fill="none" stroke="#fff" stroke-width="1"/>
          <path d="M4.5 10h11" stroke="#fff" stroke-width="1"/>
        </svg>
        <span>www.samdalton.example</span>
      </div>
    </footer>
  </main>
</body>
</html>
```